Informational Business Handout needs Company Information

We have this informational handout that we would like to start handing out to clients; however, the original designer failed to include any of our company contact information. Our main request is that you redesign this card with the appropriate contact information as listed below. We would like the information/content that is currently on the card to be on the new design as well. Feel free to take liberty with the rest of the card design, or not. Please see the card specifications and our company contact information below.

Card details: 7 x 5 inches (17.78 x 12.5 cm). Cardstock.

Company Contact Details:
Dorian Welkett, JD
TarnwickLaw, PLLC
482 E. Marlowe Ave, Ste. 310, Cedar Ridge, UT 84799
hello@tarnwicklaw-mail.com
(435) 555-0147

```html
<!DOCTYPE html>
<html lang="en">
<head>
<meta charset="utf-8">
<title>Special Needs Trust Handout – TarnwickLaw</title>
<link href="https://fonts.googleapis.com/css2?family=Poppins:wght@400;500;600&display=swap" rel="stylesheet">
<style>
  :root {
    --navy: #1f3563;
    --rust: #a5543a;
    --rust-border: #a85a3e;
    --ink: #1c2a55;
    --grey-text: #55596a;
    --paper: #ffffff;
    --backdrop: #dcdcdc;
  }
  * { margin: 0; padding: 0; box-sizing: border-box; }
  html, body { width: 1200px; height: 733px; overflow: hidden; }
  body {
    position: relative;
    background: var(--backdrop);
    font-family: "Poppins", sans-serif;
    color: var(--ink);
  }
  .card {
    position: absolute;
    top: 208px;
    width: 443px;
    height: 317px;
    background: var(--paper);
    overflow: hidden;
  }
  .card--first-party { left: 106px; border: 8px solid var(--navy); }
  .card--third-party { left: 586px; border: 8.5px solid var(--rust-border); }
  .card > * { position: absolute; }

  .card-title { color: var(--rust); text-transform: uppercase; }
  .card--first-party .card-title {
    left: 19px; top: 3px; width: 410px;
    font-size: 20.5px; line-height: 25.7px; font-weight: 600;
  }
  .card--third-party .card-title {
    left: 14px; top: 13px; width: 410px;
    font-size: 12.3px; line-height: 14.9px; font-weight: 500;
  }
  .body-text { font-size: 9.1px; line-height: 10.6px; hyphens: manual; }
  .card--first-party .intro { left: 23px; top: 58px; width: 400px; }
  .card--third-party .intro { left: 13.7px; top: 47px; width: 402px; }

  .section-label { color: var(--rust); text-transform: uppercase; }
  .card--first-party .section-label {
    left: 22px; top: 118px; font-size: 15.5px; line-height: 18px; font-weight: 600;
  }
  .card--third-party .section-label {
    left: 12px; top: 108px; font-size: 8px; line-height: 10px; font-weight: 400;
  }

  .checklist { list-style: none; }
  .checklist li {
    position: relative;
    font-size: 9.1px; line-height: 10.6px;
  }
  .checklist li::before {
    content: "";
    position: absolute; top: 1px;
    width: 8px; height: 8px;
    border: 0.8px solid var(--ink);
  }
  .card--first-party .checklist { left: 25px; top: 141px; width: 360px; }
  .card--first-party .checklist li { margin-bottom: 3.5px; padding-left: 14px; }
  .card--first-party .checklist li::before { left: 0; }
  .checklist li.follow-on { width: 245px; }
  .checklist li.follow-on::before { display: none; }
  .card--third-party .checklist { left: 12.5px; top: 125px; width: 345px; }
  .card--third-party .checklist li { margin-bottom: 10.5px; padding-left: 11px; }
  .card--third-party .checklist li::before { left: 0; top: 2px; }

  .card--first-party .closing { left: 20px; top: 257px; width: 300px; }
  .card--third-party .closing { left: 13.7px; top: 197px; width: 325px; }

  .brand-mark {
    left: 308px; top: 236px;
    display: flex; align-items: center; gap: 5px;
    font-size: 13px; font-weight: 600; color: var(--navy);
  }
  .brand-mark .brand-square { width: 10px; height: 10px; background: var(--navy); }

  .contact-name {
    left: 75px; top: 244px;
    font-size: 10.5px; line-height: 13px; color: var(--rust); font-weight: 400;
  }
  .contact-firm {
    left: 75px; top: 258px;
    font-size: 9.6px; line-height: 11px; color: var(--navy);
  }
  .contact-address, .contact-lines {
    font-size: 8.6px; line-height: 10.4px; color: var(--grey-text);
  }
  .contact-address { left: 75px; top: 270px; }
  .contact-lines { left: 252px; top: 259px; font-style: normal; }
</style>
</head>
<body>

<section class="card card--first-party">
  <h1 class="card-title">Is a first-party special needs trust right for you?</h1>
  <p class="body-text intro">Do you have a recognized disability by the social security Administration that renders you unable to engage in any substantial gainful activity by reason of any medically determined physical or mental impairment which can be expected to result in death or which has lasted or can be expected to last for a continuous period of not less than twelve months?</p>
  <h2 class="section-label">Are you...</h2>
  <ul class="checklist">
    <li>Under age 65?</li>
    <li>Expecting settlement proceeds from the negligent actions of a third party?</li>
    <li>Expecting an inheritance?</li>
    <li>Currently receiving, or will be applying for Social Security income?</li>
    <li>Currently receiving, or will be applying for Medicaid?</li>
    <li class="follow-on">Wanting to maintain or qualify for Social Security Income and/or medicaid after being awarded your settlement or inheritance?</li>
  </ul>
  <p class="body-text closing">If you have a recognized disabillity and you answered yes to any of these questions, you should contact our office to discuss whether a First-party Special Needs Trust is right for you.</p>
  <div class="brand-mark"><span class="brand-square"></span>TarnwickLaw</div>
</section>

<section class="card card--third-party">
  <h1 class="card-title">Is a third-party supplemental needs trust necessary for your estate plan?</h1>
  <p class="body-text intro">Will one of your intended beneficiaries have a recognized disabillity as determined by the Social Security Administration that renders the beneficiary unable to engage in any sub&shy;stantial gainful activity by reason of any medically determined physical or mental im&shy;pairment which can be expected to result in death or which has lasted or van be expect&shy;ed to last for a continuous period of not less than twelve months?</p>
  <h2 class="section-label">Does the intended beneficiary...</h2>
  <ul class="checklist">
    <li>Currently receive or will be applying for Social Security income?</li>
    <li>Currently receive, or plan to apply for Medicaid?</li>
    <li>Want to maintain or qualify for Social Security income and/or medicaid afer benefitting from an inheritance?</li>
  </ul>
  <p class="body-text closing">If you have an intended beneficiary with a recognized disability and you answered yes to any of these questions, you should contact our office to discuss whether a Third-Party Supplemental NeedsTrust is right for your estate plan.</p>
  <div class="contact-name">Dorian Welkett, JD</div>
  <div class="contact-firm">TarnwickLaw, PLLC</div>
  <div class="contact-address">482 E. Marlowe Ave, Ste. 310,<br>Cedar Ridge, UT 84799</div>
  <address class="contact-lines">(435) 555-0147<br>hello@tarnwicklaw-mail.com<br>www.tarnwicklaw-mail.com</address>
</section>

</body>
</html>
```